Brookvine Estates Business Card

Business Card:

Somewhere on front of card, please include Broker License Number: 5839261

Website is BrookvineEstates.com

Address is:
7216 Orchardpine Ave E
Saginaw, MI 48517

I'll let you use creative freedom on the rest; we obviously need Name, Title, Email (dana@BrookvineEstates.com), Office Phone, Cell Phone.

Don't want any special die-cutting, just a standard size business card.

On the back, include a place for the date and time of an appointment to be written in pen.

Industry/Entity Type

Business

Requirements
Must have
• Our logo, attached to email.

```html
<!DOCTYPE html>
<html lang="en">
<head>
<meta charset="utf-8">
<title>Brookvine Estates Business Card</title>
<link rel="stylesheet" href="https://fonts.googleapis.com/css2?family=Open+Sans:wght@400;600;700&display=swap">
<style>
  :root {
    --navy: #2b2a7e;
    --navy-soft: #4a4a9a;
    --grey: #bfc0c4;
    --text-grey: #8a8b90;
    --paper: #ffffff;
    --backdrop: #e9e9ec;
  }
  * { box-sizing: border-box; margin: 0; padding: 0; }
  html, body {
    width: 1200px; height: 913px; overflow: hidden;
    background: var(--backdrop);
    font-family: "Open Sans", Arial, sans-serif;
  }
  .sheet {
    width: 1200px; height: 913px;
    display: flex; flex-direction: column; align-items: center; justify-content: center; gap: 56px;
  }
  .card {
    position: relative; width: 680px; height: 388px;
    background: var(--paper); overflow: hidden;
    box-shadow: 0 6px 18px rgba(0,0,0,.14);
  }
  .card__bands { position: absolute; inset: 0; width: 100%; height: 100%; }
  .wordmark {
    position: absolute; font-weight: 700; font-size: 40px; color: var(--navy);
    letter-spacing: -0.5px; line-height: 1;
  }
  .front .wordmark { left: 44px; top: 70px; }
  .front .rule { position: absolute; left: 44px; right: 0; top: 128px; height: 1px; background: var(--navy-soft); }
  .holder { position: absolute; left: 44px; top: 196px; }
  .holder__name { font-weight: 700; font-size: 24px; color: var(--navy); letter-spacing: .3px; line-height: 1.2; }
  .holder__title {
    margin-top: 4px; padding-top: 3px; border-top: 1px solid var(--navy-soft);
    width: 260px; font-size: 13px; color: var(--text-grey); letter-spacing: 1px;
  }
  .holder__license {
    margin-top: 6px; font-size: 13px; color: var(--navy); letter-spacing: .3px;
  }
  .contact {
    position: absolute; right: 40px; top: 34px; text-align: right;
    font-size: 14px; color: var(--navy); line-height: 1.35;
  }
  .contact__address { margin-bottom: 12px; }
  .contact__lines { position: absolute; right: 0; top: 146px; width: 280px; }
  .contact__line {
    display: flex; justify-content: flex-end; align-items: center; gap: 8px;
    font-size: 14px; line-height: 1.45; white-space: nowrap;
  }
  .contact__line svg { width: 13px; height: 13px; flex: none; }
  .back .wordmark { right: 50px; top: 74px; }
  .back .rule { position: absolute; left: 300px; right: 50px; top: 126px; height: 1px; background: var(--grey); }
  .appointment { position: absolute; left: 44px; top: 168px; width: 360px; color: var(--navy); font-size: 16px; }
  .appointment__heading { font-weight: 700; font-size: 17px; margin-bottom: 10px; }
  .appointment__field { display: flex; align-items: baseline; gap: 8px; margin-bottom: 12px; font-weight: 600; }
  .appointment__blank { flex: 1; border-bottom: 2px dotted var(--navy); height: 1px; }
</style>
</head>
<body>
<main class="sheet">
  <section class="card front" aria-label="Card front">
    <svg class="card__bands" viewBox="0 0 680 388" preserveAspectRatio="none" aria-hidden="true">
      <polygon points="0,344 404,344 412,334 0,334" fill="var(--grey)"/>
      <polygon points="0,356 414,356 440,280 680,280 680,388 0,388" fill="var(--navy)"/>
    </svg>
    <div class="wordmark">Brookvine Estates</div>
    <div class="rule"></div>
    <div class="holder">
      <div class="holder__name">DANA WHITFIELD</div>
      <div class="holder__title">OWNER</div>
      <div class="holder__license">Broker License No. 5839261</div>
    </div>
    <div class="contact">
      <div class="contact__address">7216 Orchardpine Ave E<br>Saginaw, MI 48517</div>
      <div class="contact__lines">
        <div class="contact__line">+1 989-555-0142
          <svg viewBox="0 0 16 16"><path d="M4 1l3 3-2 2c1 2 3 4 5 5l2-2 3 3-2 3C7 15 1 9 1 3z" fill="var(--grey)"/></svg></div>
        <div class="contact__line">+1 989-555-0187
          <svg viewBox="0 0 16 16"><rect x="4" y="1" width="8" height="14" rx="1.5" fill="none" stroke="var(--grey)" stroke-width="1.6"/><circle cx="8" cy="12.5" r="1" fill="var(--grey)"/></svg></div>
        <div class="contact__line">dana@BrookvineEstates.com
          <svg viewBox="0 0 16 16"><rect x="1.5" y="3.5" width="13" height="9" fill="none" stroke="var(--grey)" stroke-width="1.5"/><path d="M1.5 3.5l6.5 5 6.5-5" fill="none" stroke="var(--grey)" stroke-width="1.5"/></svg></div>
        <div class="contact__line">www.BrookvineEstates.com
          <svg viewBox="0 0 16 16"><circle cx="8" cy="8" r="6.5" fill="none" stroke="var(--grey)" stroke-width="1.4"/><ellipse cx="8" cy="8" rx="2.8" ry="6.5" fill="none" stroke="var(--grey)" stroke-width="1.2"/><path d="M1.5 8h13" stroke="var(--grey)" stroke-width="1.2"/></svg></div>
      </div>
    </div>
  </section>

  <section class="card back" aria-label="Card back">
    <svg class="card__bands" viewBox="0 0 680 388" preserveAspectRatio="none" aria-hidden="true">
      <polygon points="470,318 680,318 680,308 466,308" fill="var(--grey)"/>
      <polygon points="0,296 448,296 474,330 680,330 680,388 0,388" fill="var(--navy)"/>
    </svg>
    <div class="wordmark">Brookvine Estates</div>
    <div class="rule"></div>
    <div class="appointment">
      <div class="appointment__heading">Appointment:</div>
      <div class="appointment__field">Date: <span class="appointment__blank"></span></div>
      <div class="appointment__field">Time: <span class="appointment__blank"></span></div>
    </div>
  </section>
</main>
</body>
</html>
```